Need a Sales Event Design/Logo with newspaper boilerplate. Big attention grabbing logo/type at the top with border around. Must be colorful, include artwork and be attention getting.

NAME:
Silver Pine Event
TAGLINE:
Do what car buyers recommend and get your best deal at year’s end.
CLIENT:
Brookvale Corvanta (This must be editable)
CREATIVE BRIEF:
This is a sales event for car dealership that is meant to grab eyeballs. The mental thought it should relay is that the end of the year is the very best time to buy and this is the event you should shop. You may want to tie in Alarms / Clocks / visually to help convey message.
GRAPHIC PRESENTATION:
Looking for Big Bold, Colorful attention grabbing sales event logo that can serve as a boilerplate to print or billboard advertisement. Must be able to customize with fonts embedded. Possibly 3D?
Sample attached:
FORMATS NEEDED:
Need in these formats for both CYMK & RGB: .ai *.eps * .pdf (editable) * .jpeg * .png * .psd
OWNERSHIP:
Once design has been paid for all rights to the design belong solely to purchaser in perpetuity.

Industry/Entity Type

Event

Requirements
Must have
• Must have eyepopping artwork and Event Name and Tagline.

```html
<!DOCTYPE html>
<html lang="en">
<head>
<meta charset="utf-8">
<title>Silver Pine Event – Brookvale Corvanta</title>
<link rel="stylesheet" href="https://fonts.googleapis.com/css2?family=Alfa+Slab+One&family=Bebas+Neue&display=swap">
<style>
  :root {
    --navy-deep: #1c2a6e;
    --navy: #22378f;
    --blue: #1d5fb8;
    --blue-bright: #2a86d8;
    --yellow: #fff200;
    --orange: #f7941d;
    --ink: #0a0a14;
    --white: #ffffff;
    --bevel-light: #d9d9d9;
    --bevel-dark: #4a4a4a;
  }
  html, body {
    margin: 0;
    padding: 0;
    overflow: hidden;
    background: var(--white);
  }
  .poster {
    display: block;
    width: 764px;
    height: 1200px;
  }
  .headline {
    font-family: "Alfa Slab One", serif;
    font-size: 160px;
    fill: url(#headline-fill);
    stroke: var(--ink);
    stroke-width: 14px;
    stroke-linejoin: round;
    paint-order: stroke fill;
  }
  .tagline {
    font-family: "Bebas Neue", sans-serif;
    font-size: 46px;
    fill: var(--white);
  }
  .contact {
    font-family: "Bebas Neue", sans-serif;
    font-size: 31px;
    fill: var(--white);
  }
  .phone {
    font-family: "Bebas Neue", sans-serif;
    font-size: 96px;
    fill: url(#phone-fill);
    stroke: var(--navy-deep);
    stroke-width: 6px;
    paint-order: stroke fill;
  }
</style>
</head>
<body>
<svg class="poster" viewBox="0 0 764 1200" xmlns="http://www.w3.org/2000/svg">
  <defs>
    <linearGradient id="top-band-fill" x1="0" y1="0" x2="1" y2="1">
      <stop offset="0" stop-color="var(--navy)"/>
      <stop offset="0.55" stop-color="var(--blue)"/>
      <stop offset="1" stop-color="var(--navy-deep)"/>
    </linearGradient>
    <radialGradient id="bottom-band-fill" cx="0.75" cy="0.55" r="0.8">
      <stop offset="0" stop-color="var(--blue-bright)"/>
      <stop offset="0.6" stop-color="var(--navy)"/>
      <stop offset="1" stop-color="var(--navy-deep)"/>
    </radialGradient>
    <linearGradient id="headline-fill" x1="0" y1="0" x2="1" y2="1">
      <stop offset="0.3" stop-color="var(--yellow)"/>
      <stop offset="1" stop-color="var(--orange)"/>
    </linearGradient>
    <linearGradient id="phone-fill" x1="0" y1="0" x2="1" y2="0">
      <stop offset="0.2" stop-color="var(--yellow)"/>
      <stop offset="1" stop-color="var(--orange)"/>
    </linearGradient>
    <linearGradient id="bevel-fill" x1="0" y1="0" x2="1" y2="0">
      <stop offset="0" stop-color="var(--bevel-dark)"/>
      <stop offset="0.5" stop-color="var(--bevel-light)"/>
      <stop offset="1" stop-color="var(--bevel-dark)"/>
    </linearGradient>
  </defs>

  <!-- Top band with car artwork area -->
  <polygon class="top-bevel" points="0,676 624,592 764,472 764,492 634,606 0,702" fill="url(#bevel-fill)"/>
  <polygon class="top-band" points="0,0 764,0 764,472 624,592 0,676" fill="url(#top-band-fill)"
           role="img" aria-label="Faint close-up photo of a car headlight and bodywork in blue tones"/>

  <!-- Event name -->
  <g class="event-name">
    <text class="headline" x="20" y="142" textLength="470" lengthAdjust="spacingAndGlyphs">SILVER</text>
    <text class="headline" x="20" y="284" textLength="470" lengthAdjust="spacingAndGlyphs">PINE</text>
    <text class="headline" x="20" y="426" textLength="580" lengthAdjust="spacingAndGlyphs">EVENT</text>
  </g>

  <!-- Tagline -->
  <g class="tagline-block">
    <text class="tagline" x="362" y="482" text-anchor="middle" textLength="680" lengthAdjust="spacingAndGlyphs">DO WHAT CAR BUYERS RECOMMEND AND</text>
    <text class="tagline" x="361" y="532" text-anchor="middle" textLength="610" lengthAdjust="spacingAndGlyphs">GET YOUR BEST DEAL AT YEAR’S END.</text>
  </g>

  <!-- Bottom contact band -->
  <polygon class="bottom-bevel" points="0,980 150,944 764,906 764,922 150,962 0,1000" fill="url(#bevel-fill)"/>
  <polygon class="bottom-band" points="0,1000 150,962 764,922 764,1200 0,1200" fill="url(#bottom-band-fill)"/>

  <g class="contact-block">
    <text class="contact" x="728" y="1000" text-anchor="end">WWW.BROOKVALEDRIVE.COM</text>
    <text class="phone" x="728" y="1076" text-anchor="end" textLength="576" lengthAdjust="spacingAndGlyphs">0315-482-6071</text>
    <text class="contact" x="728" y="1134" text-anchor="end" textLength="578" lengthAdjust="spacingAndGlyphs">VISIT US AT: 123 STREET, MAIN AVE., YOUR STATE, ZIP CODE</text>
    <text class="contact" x="728" y="1170" text-anchor="end">EMAIL: DRIVE@BROOKVALEDRIVE.COM</text>
  </g>
</svg>
</body>
</html>
```